PDF Document Update

Hi,

I need the attached PDF document updated.

The word document attached outlines the new format for which I want the PDF to look like.

For the "Our People" section - please remove Wilma Brackett and add in Owen Pellow (his photo is also attached).

Thanks!

```html
<!DOCTYPE html>
<html lang="en">
<head>
<meta charset="utf-8">
<title>Calder Search – Corporate Overview</title>
<link href="https://fonts.googleapis.com/css2?family=Libre+Baskerville:wght@400;700&family=Montserrat:wght@400;500;600;700&display=swap" rel="stylesheet">
<style>
:root{
  --bg:#e9eaee;
  --paper:#ffffff;
  --blue:#1a3d9e;
  --navy:#2e3582;
  --slate:#5f5f60;
  --charcoal:#2d2d2e;
  --grey:#9c9da1;
  --grey-light:#e3e3e5;
  --ink:#555659;
  --serif:"Libre Baskerville",Georgia,serif;
  --sans:"Montserrat",Arial,sans-serif;
}
*{box-sizing:border-box;margin:0;padding:0}
html,body{width:1200px;height:2245px;overflow:hidden;background:var(--bg)}
body{font-family:var(--sans);color:var(--ink)}
.stage{position:relative;width:1377px;height:2576px;transform:scale(.8715);transform-origin:0 0}
.page{position:absolute;width:530px;height:686px;background:var(--paper);overflow:hidden;box-shadow:0 3px 8px rgba(0,0,0,.18)}
.col-l{left:125px}.col-r{left:722px}
.row-1{top:182px}.row-2{top:945px}.row-3{top:1708px}
.abs{position:absolute}
.photo{position:absolute}

/* brand wordmark */
.brand{position:absolute;display:flex;align-items:center;gap:8px;font-family:var(--serif);font-weight:400;color:var(--blue);line-height:1.05}
.brand .mark{width:14px;height:14px;background:var(--blue)}
.brand .name{font-size:21px}

/* cover */
.cover-photo{left:0;top:126px;width:530px;height:496px;background:linear-gradient(120deg,#2b2f33 0%,#8f969c 40%,#d8dbdd 60%,#6d7479 80%,#b9bec1 100%)}
.cover-panel{left:0;top:395px;width:395px;height:145px;background:#fff;clip-path:polygon(0 0,100% 0,93% 100%,0 100%)}
.cover-title{left:28px;top:414px;font-family:var(--serif);font-weight:700;font-size:46px;color:var(--blue);letter-spacing:.5px;line-height:1}
.cover-sub{left:28px;top:462px;font-family:var(--serif);font-size:21px;color:var(--blue);letter-spacing:.3px}
.cover-text{left:28px;top:490px;width:330px;font-size:7px;line-height:1.45;color:#666}
.base-band{left:0;top:630px;width:530px;height:56px;background:linear-gradient(#c9c9cb,#a1a2a5)}
.slash-block{top:630px;height:56px;background:var(--blue)}

/* back cover */
.top-tab{left:0;top:27px;width:240px;height:61px;background:var(--blue);clip-path:polygon(0 0,100% 0,96% 100%,0 100%)}
.skyline{left:0;top:88px;width:530px;height:470px;background:linear-gradient(180deg,#fff 0%,#eef0f5 45%,#f4f5f8 75%,#fff 100%)}
.contact{left:55px;top:475px;font-size:9.5px;color:#333}
.contact li{list-style:none;display:grid;grid-template-columns:82px 22px 1fr;align-items:center;height:27.5px}
.contact .label{font-family:var(--serif);font-weight:700;font-size:13.5px;color:var(--blue)}
.contact .dash{width:7px;height:3px;background:var(--blue)}

/* section headers */
.tab-head{left:0;top:27px;width:148px;height:52px;background:var(--blue);clip-path:polygon(0 0,100% 0,95% 100%,0 100%);color:#fff;font-size:14px;display:flex;align-items:center;padding-left:28px;letter-spacing:.2px}
.tab-head b{font-weight:700}
.intro-band{left:140px;top:27px;width:390px;height:52px;background:var(--charcoal);clip-path:polygon(3% 0,100% 0,100% 100%,0 100%);color:#eee;font-size:6.6px;line-height:1.45;padding:7px 26px 0 26px}
.harbour{left:0;top:88px;width:530px;height:112px;background:linear-gradient(180deg,#aac3dc 0%,#d8e2ea 38%,#6e8aa3 55%,#2f5c8c 100%)}
.provides{left:42px;top:212px;display:flex;align-items:center;gap:10px}
.provides .dash{width:7px;height:3px;background:var(--blue)}
.provides h2{font-weight:400;font-size:13.5px;color:var(--charcoal);line-height:1.05}
.provides h2 b{display:block;color:var(--blue);font-weight:700}
.rule{left:27px;top:253px;width:476px;height:3px;background:#b5b6b9}
.service{left:27px;width:476px;height:59px;color:#fff;display:flex;align-items:flex-start}
.service.navy{background:var(--navy)}.service.slate{background:var(--slate)}
.service .icon{width:60px;height:59px;display:flex;align-items:center;justify-content:center;position:relative}
.service .icon::after{content:"";position:absolute;right:0;top:11px;width:1px;height:37px;background:rgba(255,255,255,.5)}
.service .copy{padding:9px 24px 0 14px}
.service h3{font-weight:400;font-size:12.5px;line-height:1.1;margin-bottom:3px}
.service h3 b{font-weight:600}
.service p{font-size:6.5px;line-height:1.4}

/* mandates */
.side-tab{left:0;top:27px;width:38px;height:61px;background:linear-gradient(#a9aaad,#8b8c90);clip-path:polygon(0 0,100% 0,70% 100%,0 100%)}
.mand-intro{left:56px;top:27px;width:430px;font-size:6.8px;line-height:1.4;color:#555}
.mand-title{left:56px;top:52px;font-size:14px;color:#222;line-height:1.1}
.mand-title b{display:flex;align-items:center;gap:9px;color:var(--blue);font-weight:700}
.mand-title b i{width:7px;height:3px;background:var(--blue)}
.team{top:97px;width:168px;height:18px;background:var(--grey-light);font-size:11.5px;color:#222;padding:2px 0 0 10px}
.team b{font-weight:600}
.mlist{top:124px;font-size:6.3px;line-height:12.1px;color:#444;list-style:none}
.mlist span{color:var(--blue)}
.vdiv{left:277px;top:103px;width:1px;height:218px;background:#ccc}
.city{left:55px;top:343px;width:475px;height:283px;background:linear-gradient(180deg,#b9c6d2 0%,#8d8f90 40%,#6f6b62 70%,#8a8c7c 100%);clip-path:polygon(0 0,100% 0,100% 100%,5% 100%)}
.footer{left:27px;top:648px;width:476px;display:flex;align-items:center;gap:12px}
.footer span{font-family:var(--serif);font-size:12.5px;letter-spacing:1.6px;color:var(--blue)}
.footer span b{font-weight:700}
.footer i{flex:1;height:2px;background:#b3b4b7}

/* people */
.people-band{left:142px;top:20px;width:388px;height:60px;background:linear-gradient(#c9c9cc,#9d9ea2);clip-path:polygon(4% 0,100% 0,100% 100%,0 100%)}
.person{top:104px;width:134px}
.portrait{position:relative;width:134px;height:118px;background:linear-gradient(180deg,#4d6a45 0%,#6e8a5e 45%,#3d4a5f 75%,#2a3552 100%)}
.portrait::after{content:"";position:absolute;right:0;bottom:0;width:0;height:0;border-style:solid;border-width:0 0 18px 134px;border-color:transparent transparent var(--blue) transparent}
.person h4{margin-top:22px;font-size:12.5px;font-weight:400;color:#222;letter-spacing:.2px}
.person h4 b{color:var(--blue);font-weight:700}
.person h5{font-size:10px;font-weight:600;color:#222;margin-top:1px}
.bio{margin-top:12px;font-size:6.3px;line-height:9.2px;color:#555}
.bio p+p{margin-top:5px}
.arch{left:198px;top:537px;width:305px;height:92px;background:linear-gradient(90deg,#d9d5cf,#f1efeb,#c9c4bc,#efece7);clip-path:polygon(0 0,100% 0,95% 100%,0 100%)}
.logo-box{left:394px;top:371px;width:109px;height:109px;background:#edeef1}
.aerial{left:27px;top:503px;width:476px;height:126px;background:linear-gradient(180deg,#9fa9ae 0%,#8d9285 45%,#5f7257 75%,#6d7a66 100%)}
</style>
</head>
<body>
<main class="stage">

  <!-- Cover -->
  <section class="page col-l row-1 cover">
    <div class="brand" style="left:212px;top:32px"><span class="mark"></span><span class="name">Calder<br>Search</span></div>
    <div class="photo cover-photo" role="img" aria-label="Upward view of a modern white-framed glass office building"></div>
    <div class="abs cover-panel"></div>
    <h1 class="abs cover-title">CALDER SEARCH</h1>
    <div class="abs cover-sub">CORPORATE OVERVIEW</div>
    <p class="abs cover-text">Calder Search is an Australian recruitment firm &amp; trusted recruitment partner to financial services firms, blue-chip corporates and professional services practices across Asia Pacific.</p>
    <div class="abs base-band"></div>
    <svg class="abs" style="left:478px;top:630px" width="52" height="56" viewBox="0 0 52 56"><polygon points="14,0 52,0 52,56 3,56" fill="#fff"/><polygon points="19,0 52,0 52,56 8,56" fill="#1a3d9e"/></svg>
  </section>

  <!-- Back cover -->
  <section class="page col-r row-1 back">
    <div class="abs top-tab"></div>
    <div class="photo skyline" role="img" aria-label="Faint city skyline backdrop"></div>
    <div class="brand" style="left:55px;top:303px"><span class="mark"></span><span class="name">Calder<br>Search</span></div>
    <ul class="abs contact">
      <li><span class="label">Call Us</span><span class="dash"></span><span>+61 (0)2 5550 1842</span></li>
      <li><span class="label">Address</span><span class="dash"></span><span>Suite 1204/88 Harbour Ln, Sydney, NSW, 2000</span></li>
      <li><span class="label">Email Us</span><span class="dash"></span><span>info@caldersearch.com.au</span></li>
      <li><span class="label">Website</span><span class="dash"></span><span>www.caldersearch.com.au</span></li>
    </ul>
    <div class="abs base-band"></div>
    <svg class="abs" style="left:0;top:630px" width="135" height="56" viewBox="0 0 135 56"><polygon points="0,0 128,0 119,56 0,56" fill="#fff"/><polygon points="0,0 122,0 113,56 0,56" fill="#1a3d9e"/></svg>
  </section>

  <!-- Who we are -->
  <section class="page col-l row-2 who">
    <div class="abs intro-band">We add value by leveraging our deep understanding of the industries, markets and disciplines that we serve, enabling us to present an informed &amp; honest approach when providing recruitment advice. We remain focused on the belief that in any recruitment process diligence, honesty and integrity will always ensure the best outcome.</div>
    <div class="abs tab-head">WHO&nbsp;<b>WE ARE</b></div>
    <div class="photo harbour" role="img" aria-label="Harbour panorama with opera house and city skyline"></div>
    <div class="abs provides">
      <svg width="32" height="32" viewBox="0 0 32 32" fill="none" stroke="#1a3d9e" stroke-width="1.4"><rect x="4" y="7" width="24" height="16" rx="1"/><path d="M12 27h8M16 23v4"/><circle cx="16" cy="5" r="2.5"/><path d="M9 13h14M9 17h9"/></svg>
      <span class="dash"></span>
      <h2>CALDER SEARCH PROVIDES<b>RECRUITMENT SERVICES THAT INCLUDE</b></h2>
    </div>
    <div class="abs rule"></div>

    <div class="abs service navy" style="top:268px">
      <div class="icon"><svg width="32" height="32" viewBox="0 0 32 32" fill="none" stroke="#fff" stroke-width="1.3"><rect x="3" y="6" width="20" height="22"/><circle cx="23" cy="9" r="5"/><path d="M13 26l4-7 4 7zM7 12h8M7 16h6"/></svg></div>
      <div class="copy"><h3><b>Contingent</b> Recruitment</h3><p>Generally most suitable for team member level hiring, where utilising our extensive database and networking skills will provide a swift outcome.</p></div>
    </div>
    <div class="abs service slate" style="top:334px">
      <div class="icon"><svg width="32" height="32" viewBox="0 0 32 32" fill="none" stroke="#fff" stroke-width="1.3"><circle cx="16" cy="7" r="3.5"/><path d="M9 17c0-4 14-4 14 0"/><circle cx="7" cy="20" r="3"/><circle cx="25" cy="20" r="3"/><path d="M2 29c0-4 10-4 10 0M20 29c0-4 10-4 10 0M16 11v6"/></svg></div>
      <div class="copy"><h3><b>Executive</b> Search</h3><p>Most suitable for specialised and/or senior leadership positions. This service is a collaborative approach that includes comprehensive market mapping which provides a high level of assurance that the best candidate in the market is selected.</p></div>
    </div>
    <div class="abs service navy" style="top:401px">
      <div class="icon"><svg width="32" height="32" viewBox="0 0 32 32" fill="none" stroke="#fff" stroke-width="1.3"><circle cx="9" cy="9" r="6"/><path d="M9 3v6h6M19 6h10M19 10h10M4 29V21M9 29V18M14 29V22"/><circle cx="22" cy="21" r="4"/><path d="M25 24l4 4"/></svg></div>
      <div class="copy"><h3><b>Market</b> Research</h3><p>Calder Search provides ancillary research services including competitor analysis, candidate pool research and salary data. This service is highly valuable when employers are in the initial planning and scoping stage prior to undertaking a recruitment campaign</p></div>
    </div>
    <div class="abs service slate" style="top:467px">
      <div class="icon"><svg width="32" height="32" viewBox="0 0 32 32" fill="none" stroke="#fff" stroke-width="1.3"><circle cx="12" cy="12" r="7"/><circle cx="12" cy="12" r="2.5"/><circle cx="22" cy="22" r="6"/><circle cx="22" cy="22" r="2"/><path d="M12 3v2M12 19v2M3 12h2M19 12h2"/></svg></div>
      <div class="copy"><h3><b>RISK</b> MANAGEMENT</h3><p>Calder Search has specialised in the risk management, compliance and legal recruitment market for 11 years. We partner with leading Australian and global corporations in the pursuit of talented employees within this rapidly changing field.</p></div>
    </div>
    <div class="abs service navy" style="top:534px">
      <div class="icon"><svg width="32" height="32" viewBox="0 0 32 32" fill="none" stroke="#fff" stroke-width="1.3"><rect x="8" y="3" width="19" height="23"/><path d="M12 9h11M12 13h11M12 17h7"/><path d="M9 19l-5 2v4c0 3 5 5 5 5s5-2 5-5v-4z"/><path d="M7 25l2 2 3-4"/></svg></div>
      <div class="copy"><h3><b>COMPLIANCE</b></h3><p>Since inception, Calder Search has completed over 500 recruitment assignments within the risk, compliance and legal area, completing over 100 successful recruitment campaigns in the last 12 months</p></div>
    </div>
    <div class="abs service slate" style="top:600px">
      <div class="icon"><svg width="32" height="32" viewBox="0 0 32 32" fill="none" stroke="#fff" stroke-width="1.3"><rect x="9" y="3" width="19" height="16"/><path d="M13 8h11M13 12h8M3 23h7l5 2h8l4-3M3 29h8l6 1 10-4"/></svg></div>
      <div class="copy"><h3><b>LEGAL</b> RECRUITMENT</h3><p>Our team of experienced consultants have deep knowledge of the dynamics of the candidate market along with the tools to be able to source candidates within this highly competitive recruitment field.</p></div>
    </div>
  </section>

  <!-- Mandates -->
  <section class="page col-r row-2 mandates">
    <div class="abs side-tab"></div>
    <p class="abs mand-intro">Please see below for the a list of recently completed recruitment assignments, followed by the profiles of the members of the Calder Search Risk.</p>
    <h2 class="abs mand-title">SELECTION OF RECENTLY COMPLETED<b>MANDATES (2021/22) <i></i></b></h2>
    <div class="abs team" style="left:53px"><b>Compliance</b> Team</div>
    <div class="abs team" style="left:306px"><b>Legal recruitment</b> Team</div>
    <ul class="abs mlist" style="left:56px">
      <li>Head of Compliance - Global Bank</li>
      <li>Director - Legal &amp; Compliance - <span>Global Fund</span></li>
      <li>Director - Internal Audit - <span>Leading Australian Bank</span></li>
      <li>VP - IBD Compliance - <span>Global Bank</span></li>
      <li>Director - Compliance Consulting - <span>Global Firm</span></li>
      <li>Director - Wealth Management Compliance Remediation</li>
      <li>Head of Client Onboarding - Global Bank</li>
      <li>Director - Control Room - Australian Bank</li>
      <li>Internal Audit Director - Leading Australian Bank</li>
      <li>Senior Manager - Technology Audit - <span>Australian Bank</span></li>
      <li>Senior Manager - Internal Audit - <span>Australian Bank</span></li>
      <li>Associate Director - Compliance - <span>Global Bank</span></li>
      <li>Manager - Internal Audit - <span>Leading Australian Bank</span></li>
      <li>Manager - Compliance - <span>Global Consulting Firm</span></li>
      <li>Compliance Manager - Retail Banking - <span>Global Bank</span></li>
      <li>Manager - Compliance Consulting - <span>Global Firm</span></li>
    </ul>
    <div class="abs vdiv"></div>
    <ul class="abs mlist" style="left:307px">
      <li>Legal &amp; Compliance Officer - Global Asset Manager</li>
      <li>Control Room Compliance Manager - Aust. Bank</li>
      <li>Credit Risk Manager - Global Bank</li>
      <li>Legal Counsel - Global Bank</li>
      <li>Manager- Wealth Management Compliance</li>
      <li>Compliance Manager - Global Bank - <span>New Zealand</span></li>
      <li>Compliance Manager - Stockbroking</li>
      <li>Legal &amp; Compliance Manager - Aust. Fund Manager</li>
      <li>Associate - Wealth Management Compliance</li>
      <li>Senior Portfolio Risk Analyst - Global Bank</li>
      <li>Internal Audit Manager - Australian Bank</li>
      <li>Legal Counsel - Global Bank</li>
      <li>Compliance Officer - Australian Stockbroking</li>
      <li>Associate - Compliance Consulting - <span>Global Firm</span></li>
      <li>AML/KYC Officer - Global Bank</li>
      <li>Legal &amp; Compliance Manager - Global Investment Bank</li>
    </ul>
    <div class="photo city" role="img" aria-label="Aerial view of downtown office towers"></div>
    <div class="abs footer"><span>www.<b>caldersearch</b>.com.au</span><i></i></div>
  </section>

  <!-- Our people 1 -->
  <section class="page col-l row-3 people">
    <div class="abs people-band"></div>
    <div class="abs tab-head">OUR&nbsp;<b>PEOPLE</b></div>

    <article class="abs person" style="left:27px">
      <div class="portrait" role="img" aria-label="Portrait of Lachlan Ward"></div>
      <h4><b>LACHLAN</b> WARD</h4>
      <h5>Director/Founder</h5>
      <div class="bio">
        <p>Lachlan has 20+ years of financial services recruitment experience, with the past 19 years assisting clients across Asia Pacific with appointing senior infrastructure and middle office staff.</p>
        <p>After graduating with a degree in Environmental Science, Lachlan spent two years in London providing recruitment services to investment banks and fund managers across a broad range of finance disciplines.</p>
        <p>In 2003 Lachlan returned to Sydney to focus on financial services recruitment within the Asia Pacific region, and managing a multi-discipline recruitment division covering risk, compliance, law, sales, marketing and corporate advisory.</p>
        <p>Lachlan founded Calder Search in 2011 as a result of client demand for a senior specialist recruitment firm with deep experience in technical markets. His recruitment strategy has involved partnering with high profile Australian and international financial services organisations, and running bespoke campaigns to identify technical skill sets and high performing professionals from manager to MD level appointments.</p>
        <p>Lachlan specialises in recruitment across the disciplines of: Compliance, operational risk, market risk, credit risk, internal audit, and law.</p>
      </div>
    </article>

    <article class="abs person" style="left:198px">
      <div class="portrait" role="img" aria-label="Portrait of Nathan Cole"></div>
      <h4><b>NATHAN</b> COLE</h4>
      <h5>Director</h5>
      <div class="bio">
        <p>Nathan has extensive experience in both executive search and contingent placement within the APAC region. After graduating with a Bachelor of Commerce, Nathan spent four years in executive search, consulting within the fixed income trading arena, where he specialised in interest rate derivative and credit derivative trading in the Asia Pacific region.</p>
        <p>Having successfully developed and maintained a significant number of high quality relationships within the investment banking industry, Nathan went on to lead a team of recruitment consultants servicing the requirements of investment banks, corporate and retail banks, fund managers and other financial service providers.</p>
        <p>As a proven leader and well-connected executive search professional, Nathan has an excellent reputation in attaining results across a wide variety of assignments.</p>
      </div>
    </article>

    <article class="abs person" style="left:369px">
      <div class="portrait" role="img" aria-label="Portrait of Oliver Grant"></div>
      <h4><b>OLIVER</b> GRANT</h4>
      <h5>Director</h5>
      <div class="bio">
        <p>Oliver completed a Mathematics degree in the UK and has over 10 years of executive search and recruitment experience specialising in the financial services and legal sectors across Asia Pacific and the United States.</p>
        <p>Oliver commenced his career as a risk management specialist with two large European banks in London. Following this Oliver spent 7 years leading risk, compliance and legal recruitment teams in Sydney. Recently Oliver was the Head of the New York office for a large global recruitment firm, driving the US recruitment strategy across the disciplines of legal, compliance and technology.</p>
        <p>Oliver brings deep expertise in both the legal and financial services industry along with the recruitment of high calibre professionals for technical roles.</p>
      </div>
    </article>

    <div class="photo arch" role="img" aria-label="Close-up of white ribbed architectural structure"></div>
    <div class="abs footer"><span>www.<b>caldersearch</b>.com.au</span><i></i></div>
  </section>

  <!-- Our people 2 -->
  <section class="page col-r row-3 people">
    <div class="abs people-band"></div>
    <div class="abs tab-head">OUR&nbsp;<b>PEOPLE</b></div>

    <article class="abs person" style="left:27px">
      <div class="portrait" role="img" aria-label="Portrait of Sam Carver"></div>
      <h4><b>SAM</b> CARVER</h4>
      <h5>Principle</h5>
      <div class="bio">
        <p>Sam joined Calder Search in 2018, and currently operates as a Principle within the Governance, Risk and Compliance division. Sam's role is focussed on assisting clients through the provision of bespoke services such as targeted headhunting and market mapping. Sam graduated with a degree in Sports &amp; Exercise Science.</p>
        <p>Sam is trained in executive search, headhunting and market mapping, he assists clients with critical support in identifying and sourcing talent, along with valuable advice on relevant industry trends, recruitment strategy and market intelligence.</p>
      </div>
    </article>

    <article class="abs person" style="left:198px">
      <div class="portrait" role="img" aria-label="Portrait of Fiona Lister"></div>
      <h4><b>FIONA</b> LISTER</h4>
      <h5>Director</h5>
      <div class="bio">
        <p>Fiona is a Principle operating within our Governance, Risk and Compliance recruitment practice. Fiona joined Calder Search after several years of professional experience gained in corporate law with a leading global law firm followed by a senior strategy position with a global retailer.</p>
        <p>Fiona has completed a significant number of high profile recruitment assignments in Australia from Analyst level appointments to Head of Legal, Company Secretary and Head of Compliance positions. Fiona is highly knowledgeable on market supply and demand dynamics, along with skilled in managing complex and sensitive senior recruitment processes.</p>
        <p>Fiona has a degree in Arts/Laws.</p>
      </div>
    </article>

    <article class="abs person" style="left:369px">
      <div class="portrait" role="img" aria-label="Portrait of Owen Pellow"></div>
      <h4><b>OWEN</b> PELLOW</h4>
      <h5>Research Associate</h5>
      <div class="bio">
        <p>Owen completed a Bachelor of Business, Management and Marketing. His role focusses on providing research assistance to our senior consultants when undertaking search assignments. This includes market mapping, headhunting and industry research campaigns.</p>
      </div>
    </article>

    <div class="abs logo-box"></div>
    <div class="brand" style="left:408px;top:405px"><span class="mark"></span><span class="name">Calder<br>Search</span></div>
    <div class="photo aerial" role="img" aria-label="Aerial view of city blocks with green rooftops"></div>
    <div class="abs footer"><span>www.<b>caldersearch</b>.com.au</span><i></i></div>
  </section>

</main>
</body>
</html>
```